Family Photography A5 Invitation to prospective clients

A restaurant will give me public space at their entrance to promote my family photography. I need an A5 vertical layout design for a card to 'invite' potential clients to call me. I am a portrait photographer in Perth, Western Australia. The A5 cards will be taken away by potential clients. They are encouraged to call the studio to register their interest with a view to having a very beautiful family portrait in the studio or on location. This will save the family $250 because the fee will be waived. Locations for photography can include a sunset at the famous Wendham Beach or parks in the Western Suburbs of Perth. Prefer Indesign work file so that I can change images for reprints later. Will be happy to give extra ongoing work to the successful designer on future projects. I'm happy to take positional images in the design and change them later.

Target Market(s)

Women mainly in the 30 to 45 years age group

Industry/Entity Type

Restaurant

Font styles to use
Sans Serif

Requirements
Must have
• Call to action and lively design that gets attention. Prefer to have some similarity with style of web site marlowimaging.com.au
Nice to have
• Prefer not to have the look of fake 'competitions' but rather an invitation to have a beautiful experience and with the opportunity to purchase a beautiful piece of art that celebrates their family. See word doc for previous idea with 'win a portrait...' Some of the words might be useful. More here... Brent Marlow’s photography hangs on thousands of walls in Perth’s homes. His family portraits are not so much photographs as works of art, each one perfect in its own way, a unique interplay of light, shade, colour and composition. They’re the ones that make people say more than just, ‘Oh, nice’. They make people linger and say, ‘Wow, amazing!’.
Should not have
• Avoid too much emphasis on cost. I am not competing on cost, but rather trying to inspire the potential client. See word doc for previous idea with 'win a portrait...' Some of the words might be useful.

```html
<!DOCTYPE html>
<html lang="en">
<head>
<meta charset="utf-8">
<title>Marlow Imaging – Portrait Session Invitation</title>
<link rel="stylesheet" href="https://fonts.googleapis.com/css2?family=Poppins:ital,wght@0,400;0,500;0,600;1,600&display=swap">
<style>
  :root {
    --backdrop: #5c0b0b;
    --backdrop-deep: #2e0303;
    --card: #ffffff;
    --band: #dedede;
    --band-light: #e9e9e9;
    --texture: #f1f1f1;
    --ink: #1f1f1f;
    --ink-soft: #3a3a3a;
    --logo-grey: #8a8a8a;
    --frame: #ffffff;
  }
  * { box-sizing: border-box; margin: 0; padding: 0; }
  html, body { width: 904px; height: 1200px; overflow: hidden; }
  body {
    font-family: "Poppins", sans-serif;
    background: radial-gradient(ellipse at center, var(--backdrop) 55%, var(--backdrop-deep) 100%);
    position: relative;
    color: var(--ink);
  }
  .card {
    position: absolute; left: 56px; top: 42px; width: 790px; height: 1116px;
    background: var(--card); overflow: hidden;
    box-shadow: 0 4px 18px rgba(0,0,0,.55);
  }
  .top-band { position: absolute; left: 0; top: 0; width: 790px; height: 76px; }
  .site-url {
    position: absolute; left: 54px; top: 18px;
    font-size: 22px; letter-spacing: 4.6px; font-weight: 400; color: var(--ink);
  }
  .texture-panel {
    position: absolute; left: 0; top: 72px; width: 388px; height: 452px;
    background: linear-gradient(180deg, var(--texture), #f7f7f7);
  }
  .photo {
    position: absolute; background: var(--frame); padding: 14px;
    box-shadow: 0 3px 10px rgba(0,0,0,.35);
  }
  .photo-fill { width: 100%; height: 100%; }
  .photo-outdoor { left: 44px; top: 136px; width: 444px; height: 306px; }
  .photo-outdoor .photo-fill { background: linear-gradient(160deg, #7f9a4a 0%, #c8a94a 45%, #6f8f3c 100%); }
  .photo-studio { left: 260px; top: 338px; width: 452px; height: 318px; transform: rotate(-3deg); }
  .photo-studio .photo-fill { background: radial-gradient(ellipse at 55% 60%, #6a6a6a 0%, #2c2c2c 60%, #1c1c1c 100%); }
  .brand-mark {
    position: absolute; left: 528px; top: 68px; width: 240px; height: 240px;
    border: 3px solid var(--logo-grey); border-radius: 50%;
    display: flex; align-items: center; justify-content: center; text-align: center;
  }
  .brand-name {
    font-size: 30px; font-weight: 500; line-height: 1.15; color: var(--logo-grey);
  }
  .headline-band {
    position: absolute; left: 0; top: 522px; width: 790px; height: 190px;
    background: linear-gradient(90deg, var(--band) 0%, var(--band-light) 100%);
  }
  .headline {
    position: absolute; left: 54px; top: 540px;
    font-size: 31px; font-weight: 600; font-style: italic; line-height: 40px; color: var(--ink);
  }
  .offer-badge { position: absolute; left: 592px; top: 560px; width: 164px; height: 164px; }
  .intro {
    position: absolute; left: 0; top: 748px; width: 790px; text-align: center;
    font-size: 19px; line-height: 27px; color: var(--ink-soft);
  }
  .invite {
    position: absolute; left: 0; top: 870px; width: 790px; text-align: center;
    font-size: 22px; font-weight: 600; font-style: italic; line-height: 32px; color: var(--ink);
  }
  .contact-band {
    position: absolute; left: 0; top: 946px; width: 790px; height: 98px; background: var(--band);
  }
  .photographer-icon {
    position: absolute; left: 218px; top: 22px; width: 66px; height: 58px;
    background: #555; border-radius: 6px;
  }
  .photographer-name {
    position: absolute; left: 294px; top: 10px;
    font-size: 37px; font-weight: 600; letter-spacing: 1px; line-height: 44px; color: var(--ink);
  }
  .phone {
    position: absolute; left: 294px; top: 52px;
    font-size: 31px; font-weight: 600; letter-spacing: 2.5px; line-height: 38px; color: var(--ink);
    display: flex; align-items: center; gap: 6px;
  }
  .addresses {
    position: absolute; left: 0; top: 1058px; width: 790px; text-align: center;
    font-size: 15px; font-weight: 600; line-height: 22px; color: var(--ink);
  }
</style>
</head>
<body>
  <main class="card">
    <svg class="top-band" viewBox="0 0 790 76" aria-hidden="true">
      <path d="M0 0 H790 V8 C740 10 720 30 690 52 C670 68 650 76 620 76 H0 Z" fill="var(--band)"/>
    </svg>
    <div class="site-url">www.marlowimaging.com.au</div>

    <div class="texture-panel" role="img" aria-label="Soft damask-style background texture"></div>

    <figure class="photo photo-outdoor">
      <div class="photo-fill" role="img" aria-label="Outdoor family portrait: a mother hugging three young boys in a park"></div>
    </figure>

    <div class="brand-mark">
      <span class="brand-name">Marlow<br>Imaging</span>
    </div>

    <div class="headline-band"></div>

    <figure class="photo photo-studio">
      <div class="photo-fill" role="img" aria-label="Studio family portrait in white shirts with the family dog on a dark backdrop"></div>
    </figure>

    <h1 class="headline">Beautiful<br>experience<br>comes with<br>the great opportunity</h1>

    <svg class="offer-badge" viewBox="0 0 164 164" aria-label="Win a free portrait session valued at $250">
      <defs>
        <radialGradient id="badgeFill" cx="40%" cy="35%" r="70%">
          <stop offset="0" stop-color="#ffffff"/>
          <stop offset="1" stop-color="#d2d2d2"/>
        </radialGradient>
      </defs>
      <circle cx="82" cy="82" r="78" fill="url(#badgeFill)" stroke="#bbb" stroke-width="1"/>
      <circle cx="82" cy="82" r="70" fill="none" stroke="#444" stroke-width="1.5" stroke-dasharray="4 3"/>
      <g transform="rotate(-22 82 82)" fill="#333" font-family="Poppins, sans-serif" text-anchor="middle">
        <text x="88" y="66" font-size="30" font-weight="500">WIN</text>
        <text x="80" y="84" font-size="16">you a</text>
        <text x="84" y="110" font-size="30" font-weight="500">FREE</text>
        <text x="84" y="126" font-size="14">portrait session</text>
        <text x="82" y="139" font-size="10">(valued at $250)</text>
      </g>
    </svg>

    <p class="intro">This is your opportunity to possess the most beautiful<br>photographic art of yourself and your loved ones. We’re<br>looking forward to giving you the experience of<br>a photography session you’ll never forget.</p>

    <p class="invite">You are invited to have a portrait session<br>with renowned local photographer</p>

    <section class="contact-band">
      <div class="photographer-icon" role="img" aria-label="Photographer with camera icon"></div>
      <div class="photographer-name">BRENT MARLOW</div>
      <div class="phone">
        <svg width="24" height="22" viewBox="0 0 24 22" aria-hidden="true">
          <path d="M3 8 C3 4 21 4 21 8 L18 10 L15 8 V6 H9 V8 L6 10 Z" fill="none" stroke="var(--ink)" stroke-width="1.8" stroke-linejoin="round"/>
          <rect x="5" y="11" width="14" height="9" rx="2" fill="none" stroke="var(--ink)" stroke-width="1.8"/>
          <circle cx="12" cy="15.5" r="2" fill="var(--ink)"/>
        </svg>
        <span>0400 555 123</span>
      </div>
    </section>

    <p class="addresses">Office Admin 18 Calder St. Westmere 6010.<br>Studio 37 Linton St. Harbourside 6159</p>
  </main>
</body>
</html>
```